Broschüre für Bauträger
Zielgruppe
Wir sind ein Bauträger für hochwertigen Wohn- und Gewerbesektor und suchen ein modernes/ hochwertiges Design.
Aufgabenstellung
Das Deckblatt für das Exposé soll die beigefügte Visualisierung des Objektes werden.
Der Text des Deckblatts soll wie folgt lauten 'Gartenhof am Erlengrund' 'Neubau von drei Mehrfamilienhäusern' 'Dresden - Leubnitz-Neuostra'. Gartenhof am Erlengrund sollte die Hauptüberschrift sein. Zudem muss das beigefügte Logo im Deckblatt integriert werden. Format DIN A4 - Querformat

```html
<!DOCTYPE html>
<html lang="de">
<head>
<meta charset="utf-8">
<title>Gartenhof am Erlengrund – Exposé</title>
<link href="https://fonts.googleapis.com/css2?family=Poppins:wght@400;500;600;700&display=swap" rel="stylesheet">
<style>
  :root {
    --maroon: #7b1f32;
    --maroon-dark: #5e1526;
    --red: #c4252f;
    --red-light: #d9434a;
    --cream: #f6e7c9;
    --ink: #3a2a30;
    --grey: #6f6b68;
    --band-grey: #8d8883;
    --band-beige: #c9bfae;
    --white: #ffffff;
  }
  html, body {
    margin: 0;
    padding: 0;
    width: 1200px;
    height: 849px;
    overflow: hidden;
    background: var(--white);
    font-family: "Poppins", sans-serif;
  }
  .cover {
    position: relative;
    width: 1200px;
    height: 849px;
    overflow: hidden;
    background: var(--white);
  }
  .building-visual {
    position: absolute;
    left: 0;
    top: 40px;
    width: 1200px;
    height: 556px;
    background: linear-gradient(180deg, #8fb9e3 0%, #cfe1f1 32%, #e3a977 55%, #d88c5a 72%, #9a9a9c 100%);
  }
  .top-band {
    position: absolute;
    left: 0;
    top: 0;
    width: 1200px;
    height: 71px;
    border-bottom-right-radius: 40px;
    background: linear-gradient(90deg, var(--red) 0%, var(--red-light) 50%, var(--red) 100%);
  }
  .bottom-band {
    position: absolute;
    left: 0;
    top: 791px;
    width: 1200px;
    height: 58px;
    border-top-left-radius: 40px;
    background: linear-gradient(90deg, var(--band-grey) 0%, var(--band-beige) 50%, var(--band-grey) 100%);
  }
  .brand {
    position: absolute;
    left: 1036px;
    top: 43px;
    width: 123px;
    height: 124px;
    box-sizing: border-box;
    background: var(--white);
    border: 3px solid var(--maroon);
    display: flex;
    align-items: center;
    justify-content: center;
    text-align: center;
    padding: 8px;
    font-size: 15px;
    font-weight: 600;
    line-height: 1.25;
    color: var(--maroon);
  }
  .title-panel {
    position: absolute;
    left: 61px;
    top: 375px;
    width: 576px;
    height: 252px;
    border-radius: 28px;
    background: var(--maroon);
    color: var(--white);
    text-align: center;
  }
  .title-panel h1 {
    margin: 0;
    position: absolute;
    left: 0;
    right: 0;
    top: 28px;
    font-size: 72px;
    font-weight: 700;
    line-height: 1.1;
    letter-spacing: 0.5px;
  }
  .subtitle {
    position: absolute;
    left: 0;
    right: 0;
    top: 121px;
    display: flex;
    align-items: center;
    justify-content: center;
    gap: 22px;
    font-size: 22px;
    font-weight: 500;
  }
  .subtitle .bar {
    display: block;
    width: 93px;
    height: 14px;
    background: var(--cream);
  }
  .subtitle .bar.right { width: 78px; }
  .project-info {
    position: absolute;
    left: 0;
    right: 0;
    top: 173px;
    margin: 0;
    font-size: 17px;
    font-weight: 500;
    line-height: 1.28;
    color: var(--cream);
  }
  .book-button {
    position: absolute;
    left: 844px;
    top: 571px;
    width: 148px;
    height: 52px;
    border-radius: 22px;
    background: var(--maroon);
    color: var(--white);
    font-size: 20px;
    font-weight: 500;
    display: flex;
    align-items: center;
    justify-content: center;
  }
  .features {
    position: absolute;
    left: 68px;
    top: 670px;
    margin: 0;
    padding: 0;
    list-style: none;
    display: grid;
    grid-template-columns: 224px 254px 220px;
    row-gap: 12px;
  }
  .features li {
    display: flex;
    align-items: center;
    gap: 10px;
    height: 36px;
    font-size: 20px;
    font-weight: 600;
    color: var(--maroon);
  }
  .features svg { flex: none; }
  .contact {
    position: absolute;
    left: 852px;
    display: flex;
    align-items: center;
    gap: 20px;
  }
  .contact.phone { top: 640px; }
  .contact.web { top: 713px; }
  .contact .label {
    font-size: 18px;
    font-weight: 500;
    color: var(--maroon);
    line-height: 1.2;
  }
  .contact .value {
    font-size: 27px;
    font-weight: 500;
    color: var(--ink);
    line-height: 1.2;
  }
  .contact .url {
    font-size: 15px;
    color: var(--ink);
    line-height: 1.3;
  }
  .contact .cta {
    font-size: 22px;
    font-weight: 600;
    color: var(--ink);
    line-height: 1.3;
  }
</style>
</head>
<body>
<main class="cover">
  <div class="building-visual" role="img" aria-label="Architekturvisualisierung der drei Mehrfamilienhäuser mit Balkonen, Straße und blauem Himmel"></div>
  <div class="top-band" role="img" aria-label="Rotes Ornamentband"></div>

  <div class="brand">Kerber Wohnbau GmbH</div>

  <section class="title-panel">
    <h1>Gartenhof</h1>
    <div class="subtitle"><span class="bar"></span><span>Am Erlengrund</span><span class="bar right"></span></div>
    <p class="project-info">Neubau von drei Mehrfamilienhäusern<br>Dresden Leubnitz Neuostra</p>
  </section>

  <div class="book-button">Book Now</div>

  <ul class="features">
    <li><svg width="26" height="26" viewBox="0 0 26 26"><circle cx="13" cy="13" r="11.5" fill="none" stroke="#6f6b68" stroke-width="2"/><path d="M8 13.5l3.3 3.3L18 10" fill="none" stroke="#6f6b68" stroke-width="2.2" stroke-linecap="round" stroke-linejoin="round"/></svg>2 Bedrooms</li>
    <li><svg width="26" height="26" viewBox="0 0 26 26"><circle cx="13" cy="13" r="11.5" fill="none" stroke="#6f6b68" stroke-width="2"/><path d="M8 13.5l3.3 3.3L18 10" fill="none" stroke="#6f6b68" stroke-width="2.2" stroke-linecap="round" stroke-linejoin="round"/></svg>Open Kitchen</li>
    <li><svg width="26" height="26" viewBox="0 0 26 26"><circle cx="13" cy="13" r="11.5" fill="none" stroke="#6f6b68" stroke-width="2"/><path d="M8 13.5l3.3 3.3L18 10" fill="none" stroke="#6f6b68" stroke-width="2.2" stroke-linecap="round" stroke-linejoin="round"/></svg>Guest Room</li>
    <li><svg width="26" height="26" viewBox="0 0 26 26"><circle cx="13" cy="13" r="11.5" fill="none" stroke="#6f6b68" stroke-width="2"/><path d="M8 13.5l3.3 3.3L18 10" fill="none" stroke="#6f6b68" stroke-width="2.2" stroke-linecap="round" stroke-linejoin="round"/></svg>4 Living Rooms</li>
    <li><svg width="26" height="26" viewBox="0 0 26 26"><circle cx="13" cy="13" r="11.5" fill="none" stroke="#6f6b68" stroke-width="2"/><path d="M8 13.5l3.3 3.3L18 10" fill="none" stroke="#6f6b68" stroke-width="2.2" stroke-linecap="round" stroke-linejoin="round"/></svg>Swimming Pool</li>
    <li><svg width="26" height="26" viewBox="0 0 26 26"><circle cx="13" cy="13" r="11.5" fill="none" stroke="#6f6b68" stroke-width="2"/><path d="M8 13.5l3.3 3.3L18 10" fill="none" stroke="#6f6b68" stroke-width="2.2" stroke-linecap="round" stroke-linejoin="round"/></svg>Natural View</li>
  </ul>

  <div class="contact phone">
    <svg width="48" height="42" viewBox="0 0 48 42">
      <circle cx="6" cy="5" r="4" fill="#7b1f32"/><rect x="18" y="2" width="30" height="5" rx="2.5" fill="#7b1f32"/>
      <circle cx="6" cy="21" r="4" fill="#7b1f32"/><rect x="18" y="18.5" width="30" height="5" rx="2.5" fill="#7b1f32"/>
      <circle cx="6" cy="37" r="4" fill="#7b1f32"/><rect x="18" y="34.5" width="30" height="5" rx="2.5" fill="#7b1f32"/>
    </svg>
    <div>
      <div class="label">More Information call us</div>
      <div class="value">000 987 654 321</div>
    </div>
  </div>

  <div class="contact web">
    <svg width="50" height="52" viewBox="0 0 50 52">
      <circle cx="22" cy="22" r="20" fill="none" stroke="#7b1f32" stroke-width="4"/>
      <path d="M4 16h36M4 28h36M22 2c-8 10-8 30 0 40M22 2c8 10 8 30 0 40" fill="none" stroke="#7b1f32" stroke-width="3"/>
      <circle cx="33" cy="34" r="9" fill="#ffffff" stroke="#7b1f32" stroke-width="4"/>
      <path d="M39.5 40.5l7 7" stroke="#7b1f32" stroke-width="5" stroke-linecap="round"/>
    </svg>
    <div>
      <div class="url">www.kerberwohnbau.example</div>
      <div class="cta">VISIT OUR WEBSITE</div>
    </div>
  </div>

  <div class="bottom-band" role="img" aria-label="Graues Ornamentband"></div>
</main>
</body>
</html>
```